Bright Harbor Counseling Letterhead for hip modern business

I would like some ombre use of the colors in the logo hip letterhead that incorporates logo colors and feel, needs to connect with young professionals and college students. i need to be able to write letters to schools to excuse absences as well. i like color blocks on one side preferably using colors from the attached logo design.

Target Market(s)

high income young people, young adults and college students

Industry/Entity Type

mental health

Font styles to use
Serif
Sans Serif

Colors
0054AA
0677BA
7BADD7
CADEEF
E8F1F8
0094D4
00A9DD
6FCCEA
C7EBF8
E9F6FB
00AB8E
00BBA5
67D7C9
C6EFE9
E9F9F6
59FF00
82FF00
B8FF75
E3FFCB
F4FFEA
A7469A
B969AE
D3A5CF
EDDBEB
F8F0F9
6B429C
8869AF
B7A5CE
E3DAEB
F3F0F8

Requirements
Must have
• a modern hip feel, somewhat color

```html
<!DOCTYPE html>
<html lang="en">
<head>
<meta charset="utf-8">
<title>Bright Harbor Counseling Letterhead</title>
<link rel="stylesheet" href="https://fonts.googleapis.com/css2?family=Jost:wght@400&display=swap">
<style>
  :root {
    --backdrop: #cae1f0;
    --paper: #e8ebf0;
    --band-light: #5fbce3;
    --band-dark: #166bb9;
    --ink: #1a1a1a;
    --wash-rose: #e4dde6;
    --wash-lilac: #e1dfe9;
  }
  * { margin: 0; padding: 0; box-sizing: border-box; }
  html, body {
    width: 1119px;
    height: 1200px;
    overflow: hidden;
    background: var(--backdrop);
  }
  .letterhead {
    position: absolute;
    left: 161px;
    top: 30px;
    width: 796px;
    height: 1140px;
    background: var(--paper);
    overflow: hidden;
  }
  .letterhead__art {
    position: absolute;
    inset: 0;
    width: 100%;
    height: 100%;
  }
  .brand {
    position: absolute;
    left: 0;
    right: 0;
    top: 120px;
    text-align: center;
    font-family: "Jost", sans-serif;
    font-weight: 400;
    font-size: 26px;
    line-height: 1;
    color: var(--ink);
  }
</style>
</head>
<body>
  <main class="letterhead">
    <svg class="letterhead__art" viewBox="0 0 1156 1656" preserveAspectRatio="none" aria-hidden="true">
      <defs>
        <linearGradient id="band-top" gradientUnits="userSpaceOnUse" x1="0" y1="0" x2="1156" y2="0">
          <stop offset="0" stop-color="var(--band-light)"/>
          <stop offset="1" stop-color="var(--band-dark)"/>
        </linearGradient>
        <linearGradient id="band-bottom" gradientUnits="userSpaceOnUse" x1="0" y1="0" x2="1156" y2="0">
          <stop offset="0" stop-color="var(--band-dark)"/>
          <stop offset="1" stop-color="var(--band-light)"/>
        </linearGradient>
        <radialGradient id="wash" cx="0.5" cy="0.5" r="0.5">
          <stop offset="0" stop-color="var(--wash-lilac)"/>
          <stop offset="0.55" stop-color="var(--wash-rose)" stop-opacity="0.8"/>
          <stop offset="1" stop-color="var(--paper)" stop-opacity="0"/>
        </radialGradient>
      </defs>

      <g class="band band--top" fill="url(#band-top)">
        <polygon points="62,0 150,0 88,71 0,71"/>
        <polygon points="167,0 256,0 194,71 106,71"/>
        <polygon points="273,0 361,0 300,71 211,71"/>
        <polygon points="378,0 1156,0 1156,71 317,71"/>
      </g>

      <rect class="watermark-area" role="img" aria-label="Faint soft-colour watermark area"
            x="80" y="440" width="1010" height="720" rx="360" fill="url(#wash)"/>

      <g class="band band--bottom" fill="url(#band-bottom)">
        <polygon points="0,1585 778,1585 839,1656 0,1656"/>
        <polygon points="795,1585 883,1585 945,1656 856,1656"/>
        <polygon points="900,1585 988,1585 1050,1656 962,1656"/>
        <polygon points="1005,1585 1093,1585 1156,1656 1067,1656"/>
      </g>
    </svg>

    <header class="brand">Bright Harbor Counseling</header>
  </main>
</body>
</html>
```